Home Page and One Inside Page Needed for Engine Modify Site

Website that sells kits to modify and enhance your car engine performance. I don't like direction / design of current site at http://www.brolvatemotors.com.php53-17.ord1-1.sitepreviewhub.com/

I want something modern. Something that shows power and performance.

I need home page and one inside page.

Keep blues and blacks and unfortunately that is their logo we have to work with. But this site needs WOW factor.

YOU DO NOT HAVE PERMISSION TO WORK OR SPEAK TO CLIENT DIRECTLY AND MUST WORK THROUGH ME.

```html
<!DOCTYPE html>
<html lang="en">
<head>
<meta charset="utf-8">
<title>brolvatemotors – How It Works</title>
<link href="https://fonts.googleapis.com/css2?family=PT+Sans:wght@400;700&family=Arimo:wght@400;700&display=swap" rel="stylesheet">
<style>
:root{
  --blue:#0a14e6;
  --ink:#111;
  --dark:#2e2e2e;
  --footer:#333;
  --page:#f1f1f1;
  --panel:#f6f6f6;
  --text:#7a7a7a;
  --slate:#5b7fa3;
  --line:#d4d4d4;
}
*{margin:0;padding:0;box-sizing:border-box}
html,body{width:998px;height:1200px;overflow:hidden}
body{position:relative;background:var(--page);font-family:"PT Sans",sans-serif;color:var(--text)}
.abs{position:absolute}

/* header */
.header{left:0;top:0;width:998px;height:58px;background:#fff}
.header-bar{left:0;top:0}
.brand{left:157px;top:6px;color:var(--blue);font:700 28px/1 "PT Sans",sans-serif;letter-spacing:-.3px}
.tagline{left:157px;top:36px;color:#222;font-size:9px;letter-spacing:.1px}
.nav{left:426px;top:19px;display:flex;align-items:center;height:20px}
.nav a{color:#fff;text-decoration:none;font-size:12px;padding:0 9px;line-height:20px;position:relative}
.nav .sep{color:#777;font-size:13px;transform:skewX(-10deg)}
.nav a.active{padding:0 17px}
.nav a.active::before{content:"";position:absolute;inset:0;background:var(--blue);transform:skewX(-20deg);z-index:-1}

/* hero */
.hero{left:0;top:58px;width:998px;height:292px;background:linear-gradient(100deg,#3a3a3a 0%,#555 30%,#4a4a4a 60%,#3c3c3c 100%)}
.hero-text{left:184px;top:156px;width:275px;color:#fff;font-size:11.2px;line-height:14.3px}
.tab-title{left:170px;top:326px;font:700 18px/1 "Arimo",sans-serif;color:var(--ink)}
.tab-title span{color:var(--slate)}

/* content */
.content{left:157px;top:350px;width:684px;height:620px;background:var(--panel)}
.stage-line{left:157px;width:445px;height:1px;background:var(--line)}
.stage-head{display:flex;align-items:center;font:700 15px/1 "Arimo",sans-serif;color:var(--ink);height:33px}
.stage-head .num{display:inline-block;margin:0 10px 0 7px}
.copy{left:170px;width:423px;font-size:8.9px;line-height:12.8px;text-align:justify;color:var(--text)}
.photo{float:left;width:165px;height:106px;border:1px solid #ddd;background:#fff;padding:3px;margin:0 12px 2px 0}
.photo div{width:100%;height:100%}
.rail{left:616px;width:1px;background:#888}
.rail-mark{left:612px;width:8px;background:var(--blue)}

/* sidebar */
.side-head{left:643px;width:198px;height:35px}
.side-head h3{position:absolute;left:14px;top:10px;font:700 15px/1 "Arimo",sans-serif;color:#fff}
.news{left:643px;width:196px;background:#fff;border:1px solid #ddd;padding:8px 10px;font-size:9.3px;line-height:12.9px;color:#222}
.date{left:643px;width:80px;height:22px}
.date span{position:absolute;left:6px;top:5px;color:#fff;font-size:10px}
.links{left:646px;top:764px;width:190px;list-style:none}
.links li{height:22.8px;border-bottom:1px dashed #bbb;font-size:9.3px;line-height:22px;color:#666;padding-left:11px;position:relative}
.links li::before{content:"→";position:absolute;left:0;font-size:8px;color:#555}
.links li.current{color:var(--blue)}

/* footer */
.footer{left:0;top:992px;width:998px;height:150px;background:var(--footer);color:#aaa}
.footer h4{position:absolute;top:12px;font-weight:400;font-size:13.5px;color:#fff}
.foot-nav{position:absolute;left:156px;top:35px;list-style:none}
.foot-nav li{font-size:9.6px;line-height:17.9px;padding-left:13px;position:relative;color:#888}
.foot-nav li::before{content:"→";position:absolute;left:0;font-size:8px}
.foot-nav li.current{color:#fff}
.social{position:absolute;left:336px;width:102px;height:24px}
.social span{position:absolute;left:32px;top:6px;color:#222;font-size:10px}
.address{position:absolute;left:498px;top:38px;font:400 9.3px/14.3px "Arimo",sans-serif;color:#aaa}
.email-field{position:absolute;left:658px;top:38px;width:182px;height:21px;border:1px solid #444;background:#2b2b2b;color:#666;font-size:9.5px;padding:4px 7px}
.copyright{left:0;top:1142px;width:998px;height:58px;text-align:center;font-size:9px;color:#222;padding-top:16px}
</style>
</head>
<body>

<!-- header -->
<div class="abs header"></div>
<svg class="abs header-bar" width="998" height="65" viewBox="0 0 998 65" aria-hidden="true">
  <polygon points="376,0 998,0 998,65 406,65 401,58 0,58 0,57 400,57" fill="#000"/>
</svg>
<div class="abs brand">brolvatemotors</div>
<div class="abs tagline">precision exhaust header modeling system</div>
<nav class="abs nav">
  <a href="#">Home</a><span class="sep">\</span>
  <a href="#">About Us</a><span class="sep">\</span>
  <a href="#">Product</a><span class="sep">\</span>
  <a href="#">Resources</a>
  <a href="#" class="active">How It Works</a>
  <a href="#">Contact Us</a>
</nav>

<!-- hero -->
<div class="abs hero" role="img" aria-label="Background photo of an engine bay"></div>
<svg class="abs" style="left:157px;top:100px" width="684" height="214" viewBox="0 0 684 214" aria-hidden="true">
  <defs>
    <radialGradient id="heroGlow" cx="0.65" cy="0.45" r="0.6">
      <stop offset="0" stop-color="#1e3ab8"/>
      <stop offset="0.55" stop-color="#0c1560"/>
      <stop offset="1" stop-color="#04061e"/>
    </radialGradient>
  </defs>
  <polygon points="0,0 684,0 684,213 467,213 442,170 0,170" fill="url(#heroGlow)" stroke="#8a8a8a" stroke-width="1"/>
</svg>
<div class="abs" style="left:492px;top:120px;width:310px;height:180px;border-radius:40%;background:radial-gradient(ellipse at center,#c9ccd6 0%,#8d93a8 40%,rgba(40,55,130,0) 72%)" role="img" aria-label="Product photo of a polished stainless exhaust system with four tips"></div>
<p class="abs hero-text">Lorem Ipsum is simply dummy text of the printing and typesetting industry. Lorem Ipsum has been the industry's standard dummy. pesetting industry. Lorem Ipsum been the industry's standard.</p>

<!-- title tab -->
<svg class="abs" style="left:157px;top:313px" width="294" height="38" viewBox="0 0 294 38" aria-hidden="true">
  <polygon points="0,0 266,0 294,37 0,37" fill="var(--panel)"/>
</svg>
<div class="abs" style="left:0;top:350px;width:998px;height:8px;background:#fff"></div>
<div class="abs content"></div>
<div class="abs tab-title"><span>How It</span> WORK</div>

<!-- stage 1 -->
<div class="abs stage-line" style="top:388px"></div>
<svg class="abs" style="left:186px;top:372px" width="296" height="33" viewBox="0 0 296 33" aria-hidden="true">
  <polygon points="8,0 288,0 296,16.5 288,33 8,33 0,16.5" fill="#e2e2e2" stroke="#d2d2d2"/>
</svg>
<div class="abs stage-head" style="left:202px;top:372px">STAGE
  <svg class="num" width="25" height="20" viewBox="0 0 25 20" aria-hidden="true"><polygon points="0,0 20,0 25,10 20,20 0,20" fill="#000"/><text x="9.5" y="15.5" fill="#fff" font-family="Arimo,sans-serif" font-weight="700" font-size="15" text-anchor="middle">1</text></svg>
  DESIGN AND MODELING</div>
<div class="abs copy" style="top:417px">
  <div class="photo"><div style="background:linear-gradient(135deg,#e07a3a,#c9602a 45%,#e9d8cc)" role="img" aria-label="Photo of orange plastic modeling blocks"></div></div>
  Regardless of the engine type, exhaust and engine builders are presented with a very challenging spatial problem when designing a tubular exhaust header system. Multiple complex branches made of arbitrary straight and bent sections of preset ODs and lengths have to be arranged in the best possible way to create a compact package that is also easy to fabricate. But determining which one is the best layout among all the possible pathway combinations the runners can follow is the real challenge . If we define the solution to this problem as devising a method to explore as many combinations as possible and zeroing in on the most feasible, at minimal cost and in the shortest period of time, a strategy to tackle it can then be drawn.<br>
  By breaking up the overall solution to this problem into a finite number of partial solutions that can be solved one by one, the design problem is dramatically simplified. brolvatemotorsTM , earning various patents in the process, has successfully turned these partial solutions in our problem into modular, interconnecting straight and curved plastic modeling elements or blocks of certain OD and same length that faithfully represent round metal sections in an exhaust header design. This is Stage 1 of brolvatemotorsTM precision exhaust header modeling systems.
</div>
<div class="abs rail" style="top:404px;height:241px"></div>
<div class="abs rail-mark" style="top:404px;height:74px"></div>

<!-- stage 2 -->
<div class="abs stage-line" style="top:683px"></div>
<svg class="abs" style="left:186px;top:667px" width="326" height="33" viewBox="0 0 326 33" aria-hidden="true">
  <polygon points="8,0 318,0 326,16.5 318,33 8,33 0,16.5" fill="#e2e2e2" stroke="#d2d2d2"/>
</svg>
<div class="abs stage-head" style="left:202px;top:667px">STAGE
  <svg class="num" width="25" height="20" viewBox="0 0 25 20" aria-hidden="true"><polygon points="0,0 20,0 25,10 20,20 0,20" fill="#000"/><text x="9.5" y="15.5" fill="#fff" font-family="Arimo,sans-serif" font-weight="700" font-size="15" text-anchor="middle">2</text></svg>
  FABRICATION AND WELDING</div>
<div class="abs copy" style="top:717px">
  <div class="photo"><div style="background:linear-gradient(135deg,#1a1a1a,#5a5a5a 40%,#222 70%,#777)" role="img" aria-label="Photo of bent black metal exhaust tubes"></div></div>
  J- or U-bends are all it takes to turn designs modeled with plastic blocks into a full metal version thanks to the fabricating tools brolvatemotorsTM has developed to complement the system (for more info see the header fabrication tools page). Partial angle bends are no longer necessary, which drastically reduces your required metal inventory. By utilizing precision U-, or J-bends of matching CLR, available from exhaust components suppliers, it is very easy to transfer your design model into metal, section by section. Using a vertical band saw (10" or more of throat capacity) for metal cutting, the brolvatemotorsTM aluminum Pivoting Table attachment (p/n PTX1000) and the HDPE plastic Tube-Cutting Spacers (Series or tubing OD specific) simplify the task of accurately cutting the bent sections. Then, the innovative tack-welding clamps become extra sets of precise hands that don't get burned or tired, and while keeping a firm hold of the tubular sections to be welded.<br>
  The fabrication process starts by recording your design information, section by section, on the provided Metal Control Sheets. These become the blueprints and shopping list for your specific design. They are also the way to do repeats later on of the same design. Then, each section according to the list is cut by creating and placing an equivalent section made of blocks, on the PTX1000 and around a CLR-matching Cutting Spacer.
</div>
<div class="abs rail" style="top:717px;height:235px"></div>
<div class="abs rail-mark" style="top:717px;height:34px"></div>

<!-- sidebar -->
<svg class="abs side-head" style="top:391px" viewBox="0 0 198 35" aria-hidden="true"><polygon points="0,0 178,0 198,35 0,35" fill="var(--dark)"/><path d="M155 12l-4 5.5 4 5.5M167 12l4 5.5-4 5.5" stroke="#fff" stroke-width="2" fill="none"/></svg>
<div class="abs side-head" style="top:391px"><h3>LATEST NEWS</h3></div>

<div class="abs news" style="top:435px;height:82px">Lorem Ipsum is simply dummy text of the printing and typesetting industry. Lorem Ipsum has been the industry's standard dummy. pesetting industry. Lorem Ipsum been the industry's standard</div>
<svg class="abs" style="left:668px;top:516px" width="14" height="14" viewBox="0 0 14 14" aria-hidden="true"><polygon points="0,0 12,0 2,13" fill="#fff" stroke="#ddd"/><line x1="0.5" y1="0.5" x2="11.5" y2="0.5" stroke="#fff" stroke-width="2"/></svg>
<svg class="abs date" style="top:537px" viewBox="0 0 80 22" aria-hidden="true"><polygon points="0,0 65,0 80,22 0,22" fill="var(--blue)"/></svg>
<div class="abs date" style="top:537px"><span>17 July 2013</span></div>

<div class="abs news" style="top:568px;height:82px">Lorem Ipsum is simply dummy text of the printing and typesetting industry. Lorem Ipsum has been the industry's standard dummy. pesetting industry. Lorem Ipsum been the industry's standard</div>
<svg class="abs" style="left:668px;top:649px" width="14" height="14" viewBox="0 0 14 14" aria-hidden="true"><polygon points="0,0 12,0 2,13" fill="#fff" stroke="#ddd"/><line x1="0.5" y1="0.5" x2="11.5" y2="0.5" stroke="#fff" stroke-width="2"/></svg>
<svg class="abs date" style="top:670px" viewBox="0 0 80 22" aria-hidden="true"><polygon points="0,0 65,0 80,22 0,22" fill="var(--blue)"/></svg>
<div class="abs date" style="top:670px"><span>18 July 2013</span></div>

<svg class="abs side-head" style="top:715px" viewBox="0 0 198 35" aria-hidden="true"><polygon points="0,0 178,0 198,35 0,35" fill="var(--dark)"/><path d="M155 12l-4 5.5 4 5.5" stroke="#fff" stroke-width="2" fill="none"/><path d="M167 12l4 5.5-4 5.5" stroke="var(--blue)" stroke-width="2" fill="none"/></svg>
<div class="abs side-head" style="top:715px"><h3>LATEST NEWS</h3></div>
<ul class="abs links">
  <li class="current">1625 Series Products</li>
  <li>1750 Series Products</li>
  <li>2000 Series Products</li>
  <li>Fabrication Tools</li>
  <li>Pre-Bent Tubing</li>
  <li>Other Products</li>
</ul>

<!-- footer -->
<footer class="abs footer">
  <h4 style="left:156px">Navigation</h4>
  <ul class="foot-nav">
    <li class="current">Home</li>
    <li>About Us</li>
    <li>Product</li>
    <li>Resources</li>
    <li>How It Works</li>
    <li>Contact Us</li>
  </ul>

  <h4 style="left:332px">Connect with Us</h4>
  <div class="social" style="top:36px"><svg width="102" height="24" viewBox="0 0 102 24" aria-hidden="true"><polygon points="0,0 88,0 102,24 0,24" fill="#e8e8e8"/><rect x="6" y="4" width="16" height="16" fill="#222"/></svg><span>Friendspace</span></div>
  <div class="social" style="top:67px"><svg width="102" height="24" viewBox="0 0 102 24" aria-hidden="true"><polygon points="0,0 88,0 102,24 0,24" fill="#e8e8e8"/><rect x="6" y="4" width="16" height="16" fill="#222"/></svg><span>Chirpline</span></div>
  <div class="social" style="top:98px"><svg width="102" height="24" viewBox="0 0 102 24" aria-hidden="true"><polygon points="0,0 88,0 102,24 0,24" fill="#e8e8e8"/><rect x="6" y="4" width="16" height="16" fill="#222"/></svg><span>Clipstream</span></div>

  <h4 style="left:497px">Contact Address</h4>
  <p class="address">482 Marlow Ridge Road Austin,<br>TX 78745<br>Phone: (512) 555 0147<br>Fax: (512) 555 0193<br>M-F 9-6<br>Email: info@brolvatemotors.com</p>

  <h4 style="left:658px">Subscribe for News Letter</h4>
  <div class="email-field">Your E-mail ID</div>
  <svg class="abs" style="left:658px;top:66px" width="77" height="20" viewBox="0 0 77 20" aria-hidden="true"><polygon points="0,0 64,0 77,20 0,20" fill="#e8e8e8"/></svg>
  <div class="abs" style="left:669px;top:70px;font:400 10px/1 'Arimo',sans-serif;color:#111">Subscribe</div>
</footer>
<div class="abs copyright">2013 © Brolvatemotors. All rights Reserved.</div>

</body>
</html>
```